Flyer-Design für Marktplatz der bäuerlichen Landwirtschaft
Zielgruppe
Der stilleWiesenhof stellt einen Marktplatz der bäuerlichen Landwirtschaft zur Verfügung.
Zielgruppe 1: Lieferanten, bäuerliche Direktvermarkter mit herausragenden Produkten die für eine weitere Vertriebsmöglichkeit für Ihre Produkte offen sind.
Zielgruppe 2: Kunden, die auf der Suche nach mit Liebe hergestellten Produkten aus der bäuerlichen Landwirtschaft sind. Sie sind bereit für ein gutes Produkt auch einen entsprechenden Preis zu zahlen.
Aufgabenstellung
Es soll ein Flyer im Postkartenformat DIN A6 – quer designt werden.
Das Ergebnis soll sowohl, als Datei direkt der Druckerei übergeben werden und auch im eps-Format bereitgestellt werden. Auf Hinweis eines Designers das es ggf. schwer wird die Datei im EPS bereitzustellen könnten wir darauf auch verzichten.
Wir haben unser Logo und die Schriftart als Dateien zur Verfügung gestellt.
Der Eindruck soll sehr hochwertig sein und dabei Bodenständigkeit ausdrücken. Das Design soll sehr elegant sein, wobei ein wenig Verspieltheit in Ordnung ist. Bitte darauf achten, dass an den Seitenrändern einen Sicherheitsabstand von 4mm für Schrift oder Logo eingehalten werden muss.
Auf Seite 1 sollen folgende Objekte platziert werden:
• Logo – (Hier kann die Anordnung der Schriftzüge „stiller“ und „Wiesenhof“ gerne noch optimiert werden.)
• Slogan: „Marktplatz der bäuerlichen Landwirtschaft“
• Internetadresse: www.stillerWiesenhof-beispiel.de
Als Hintergrundfarbe wünschen wir uns eine pastellige lindgrüne Hintergrundfarbe.
Auf Seite 2 sollen folgende Objekte platziert werden:
• Ein Block / Bereich, der ca. 1/3 der Seite ausmacht, der abgesetzt ist um eine persönliche Ansprache zu ermöglichen (Entweder Stempel oder handschriftliche Ansprache). Dieser Block sollte mit „Für Dich“ überschrieben sein (Gerne auch eine andere gute offene Überschrift für den Block nutzen)
• Hier können wir uns eine Mischung aus pastelligem Grau und Blau vorstellen (Gerne auch eine eigene pastellige Ideen einbringen)
• Jetzt fehlt uns nur noch ein Satz, der die Betrachter zum Besuch der Webseite einladen soll. Der im übrigen Teil dargestellt werden soll.
• Je nach Design kann evtl. das Logo in einer kleineren Darstellung mit integriert werden.
Für Rückfragen stehen wir gerne zur Verfügung.
Wir freuen uns auf Eure Entwürfe

```html
<!DOCTYPE html>
<html lang="de">
<head>
<meta charset="utf-8">
<title>Für Dich – Marktplatz der bäuerlichen Landwirtschaft</title>
<link rel="stylesheet" href="https://fonts.googleapis.com/css2?family=Ubuntu:wght@500;700&display=swap">
<style>
  :root {
    --page-bg: #d9d9d9;
    --lime-light: #d6f7b0;
    --lime-mid: #9fd870;
    --lime-deep: #5f9e2c;
    --leaf-green: #5a9a2a;
    --white: #ffffff;
    --pin-red: #e0231c;
    --text-shadow: rgba(40, 70, 20, 0.75);
  }
  * { box-sizing: border-box; margin: 0; padding: 0; }
  html, body {
    width: 1200px; height: 676px; overflow: hidden;
    background: var(--page-bg);
    font-family: "Ubuntu", sans-serif;
  }
  .flyer {
    position: absolute; left: 150px; top: 19px;
    width: 900px; height: 638px; overflow: hidden;
  }
  .market-backdrop {
    position: absolute; inset: 0;
    background:
      radial-gradient(ellipse at 0% 0%, var(--lime-light) 0%, rgba(214,247,176,0) 45%),
      linear-gradient(135deg, var(--lime-mid) 0%, #86c653 45%, var(--lime-deep) 100%);
  }
  .brand-name {
    position: absolute; left: 20px; top: 140px;
    font-size: 11px; font-weight: 700; color: var(--leaf-green);
    transform: rotate(-90deg); transform-origin: left top;
    white-space: nowrap;
  }
  .speech-bubble {
    position: absolute; left: 86px; top: 28px; width: 212px; height: 96px;
  }
  .speech-bubble__title {
    position: absolute; left: 0; top: 0; width: 100%; height: 88px;
    display: flex; align-items: center; justify-content: center;
    font-size: 36px; font-weight: 700; color: var(--leaf-green);
  }
  .slogan {
    position: absolute; left: 371px; top: 20px;
    font-size: 31px; font-weight: 500; line-height: 40px;
    color: var(--white);
    text-shadow: 1px 1px 0 var(--text-shadow), -1px 0 0 var(--text-shadow), 0 2px 3px var(--text-shadow);
    white-space: nowrap;
  }
  .greeting-card {
    position: absolute; left: 33px; top: 164px; width: 417px; height: 339px;
    background: var(--white);
    box-shadow: 2px 3px 6px rgba(30, 60, 10, 0.35);
  }
  .push-pin { position: absolute; left: 418px; top: 146px; width: 34px; height: 46px; }
  .invitation {
    position: absolute; left: 418px; top: 520px;
    transform: rotate(-12deg); transform-origin: 0 100%;
    color: var(--white); font-weight: 700;
    text-shadow: 0 2px 3px var(--text-shadow);
    white-space: nowrap;
  }
  .invitation__line { font-size: 27px; line-height: 32px; }
  .invitation__url { font-size: 21px; line-height: 28px; padding-left: 84px; }
  .heart { position: absolute; width: 20px; height: 18px; }
  .heart--top { left: 850px; top: 452px; }
  .heart--bottom { left: 430px; top: 617px; }
</style>
</head>
<body>
  <main class="flyer">
    <div class="market-backdrop" role="img" aria-label="Grün getöntes Foto eines Wochenmarkts mit Ständen, Kisten und Gemüse"></div>

    <span class="brand-name">stilleWiesenhof</span>

    <div class="speech-bubble">
      <svg width="212" height="96" viewBox="0 0 212 96" aria-hidden="true">
        <path d="M106 2 C165 2 206 20 206 46 C206 72 165 90 106 90 C70 90 42 84 26 73 L2 80 L14 62 C8 57 6 52 6 46 C6 20 48 2 106 2 Z"
              fill="#ffffff" stroke="#e6f2d8" stroke-width="1"/>
      </svg>
      <div class="speech-bubble__title">Für Dich!</div>
    </div>

    <h1 class="slogan">Marktplatz für Produkte aus<br>der bäuerlichen Landwirtschaft</h1>

    <section class="greeting-card" aria-label="Feld für persönliche Ansprache"></section>

    <svg class="push-pin" viewBox="0 0 34 46" aria-hidden="true">
      <line x1="13" y1="26" x2="5" y2="44" stroke="#9a9a9a" stroke-width="2.5" stroke-linecap="round"/>
      <ellipse cx="16" cy="24" rx="11" ry="5" fill="#b5140f" transform="rotate(25 16 24)"/>
      <rect x="14" y="9" width="9" height="14" rx="3" fill="var(--pin-red)" transform="rotate(25 18 16)"/>
      <ellipse cx="22" cy="9" rx="10" ry="6" fill="var(--pin-red)" transform="rotate(25 22 9)"/>
      <ellipse cx="20" cy="7" rx="3" ry="2" fill="#ff8a80"/>
    </svg>

    <div class="invitation">
      <p class="invitation__line">Wir freuen uns auf Dich unter:</p>
      <p class="invitation__url">www.stillerWiesenhof-beispiel.de</p>
    </div>

    <svg class="heart heart--top" viewBox="0 0 20 18" aria-hidden="true">
      <path d="M10 17 C4 12 1 9 1 5.5 C1 2.5 3.5 1 5.5 1 C7.5 1 9 2.5 10 4 C11 2.5 12.5 1 14.5 1 C16.5 1 19 2.5 19 5.5 C19 9 16 12 10 17 Z" fill="#ffffff"/>
    </svg>
    <svg class="heart heart--bottom" viewBox="0 0 20 18" aria-hidden="true">
      <path d="M10 17 C4 12 1 9 1 5.5 C1 2.5 3.5 1 5.5 1 C7.5 1 9 2.5 10 4 C11 2.5 12.5 1 14.5 1 C16.5 1 19 2.5 19 5.5 C19 9 16 12 10 17 Z" fill="#ffffff"/>
    </svg>
  </main>
</body>
</html>
```